Shopify Design for wedding invitations

We are a greeting card manufactory, special in wedding invitation
I need a shopify website for our wedding invitation brand. (Lovonna), atttach you can find our logo.
We are looking for someone to create a modern and clean looking e-commerce store for our wedding invitation through Shopify. We need some life, professionalism and style put into our site. We will have a variety serie of products : laser cut wedding invitation, popup wedding invitaiton, vintage wedding invitation, handmade wedding invitation, printing invitation, Custom wedding cards, wedding stationery (including favor box, table card, place card, escort card, number card), Thank you card. our online store requires easy navigation to categories divided by product type.

our market is , Eourpe and USA,
please choose a good color for it.
you can go to our website: www.bluepinecrafts.com and check our product.
also you can go to Shopvane 4 new items.
https://www.shopvane.com/dp/K47T8M2Q61?ref=myi_title_dp

Designs look the same

Target Market(s)

Europe and USA

Industry/Entity Type

wedding

Number of Pages Required

1 page

Requirements
Must have
• Logo, 3 banners than can be changed each 3-5 seconds.
Nice to have
• nice icon and font, beautiful color,

```html
<!DOCTYPE html>
<html lang="en">
<head>
<meta charset="utf-8">
<title>Lovonna – Wedding Invitations</title>
<link rel="stylesheet" href="https://fonts.googleapis.com/css2?family=Jost:wght@400;500;600&display=swap">
<style>
:root{
  --brown-dark:#4a2a1a;
  --brown:#5c3520;
  --brown-mid:#7a4a2e;
  --red:#e4131c;
  --ink:#1c1c1c;
  --muted:#555;
  --line:#e4e4e4;
  --white:#fff;
}
*{margin:0;padding:0;box-sizing:border-box}
html,body{width:1200px;height:4052px;overflow:hidden;background:var(--white)}
body{position:relative;font-family:'Jost',sans-serif;color:var(--ink)}
.abs{position:absolute}
.topbar{left:0;top:0;width:1200px;height:44px;background:var(--brown-dark);color:#f3e8e0;font-size:12px;text-align:center;line-height:44px}
.topbar .close{position:absolute;right:22px;top:0;font-size:14px}
.header{left:0;top:44px;width:1200px;height:82px;border-bottom:1px solid var(--line)}
.brand{font-size:34px;font-weight:500;color:var(--brown);letter-spacing:.5px}
.header .brand{position:absolute;left:86px;top:18px}
.nav{position:absolute;left:463px;top:32px;display:flex;gap:26px;font-size:15px}
.icons{position:absolute;left:955px;top:30px;display:flex;gap:22px}
.icons svg{width:22px;height:22px;stroke:var(--ink);fill:none;stroke-width:1.6}
.cart-badge{position:absolute;left:1098px;top:25px;width:14px;height:14px;border-radius:50%;background:var(--brown-dark);color:#fff;font-size:9px;text-align:center;line-height:14px}
.hero-left{left:0;top:126px;width:600px;height:478px;background:linear-gradient(135deg,#b8a596,#8e7565 60%,#a8927f)}
.hero-left::after{content:"";position:absolute;inset:0;background:rgba(255,255,255,.35)}
.hero-right{left:600px;top:126px;width:600px;height:478px;background:radial-gradient(circle at 55% 50%,#d9b98a,#a87444 45%,#5a3220 90%)}
.hero-copy{left:86px;top:222px;width:420px;z-index:2}
.hero-copy h1{font-size:54px;font-weight:600;line-height:1.18;color:#111}
.hero-copy p{font-size:15px;line-height:1.55;margin-top:18px;color:#222}
.btn{display:inline-block;background:var(--red);color:#fff;border-radius:24px;font-size:15px;padding:0 32px;height:44px;line-height:44px}
.hero-copy .btn{margin-top:22px}
.dots{left:86px;top:560px;display:flex;gap:8px;z-index:2}
.dots i{display:block;width:34px;height:3px;background:rgba(230,40,40,.35)}
.dots i:first-child{background:var(--red)}
.section-title{left:0;width:1200px;text-align:center;font-size:36px;font-weight:500}
.cat{width:326px;height:291px;overflow:hidden}
.cat::after{content:"";position:absolute;inset:0;background:linear-gradient(to top,rgba(70,30,15,.85),rgba(70,30,15,0) 55%)}
.cat span{position:absolute;left:23px;bottom:42px;color:#fff;font-size:17px;z-index:2}
.cat b{position:absolute;left:23px;bottom:18px;z-index:2}
.about{left:86px;top:1480px;width:1027px;height:281px;background:linear-gradient(135deg,#6b3c22,#5c3520 50%,#744528);color:#f5ebe3;text-align:center;padding:50px 90px 0}
.about h2{font-size:36px;font-weight:500;color:#fff;margin-bottom:20px}
.about p{font-size:12.5px;line-height:1.7;margin-bottom:10px}
.prod{width:237px}
.prod .img{height:239px}
.prod .name{font-size:12.5px;line-height:1.6;margin-top:11px;height:42px}
.prod .price{font-size:13px;font-weight:600;color:var(--brown);margin-top:8px}
.video{left:0;top:2707px;width:1200px;height:490px;background:linear-gradient(90deg,#6a5144,#8a6e5e 50%,#6e5546)}
.play{left:550px;top:2904px;width:96px;height:96px;border-radius:50%;background:#fff;box-shadow:0 0 0 10px rgba(255,255,255,.25)}
.blog{height:265px;background:#fff;box-shadow:0 4px 20px rgba(0,0,0,.08)}
.blog .img{position:absolute;left:0;top:0;width:236px;height:265px}
.blog .txt{position:absolute;left:263px;top:32px;width:210px}
.blog .date{font-size:13px;color:var(--muted);display:flex;align-items:center;gap:6px}
.blog h3{font-size:15px;font-weight:600;line-height:1.45;margin:10px 0 18px}
.blog p{font-size:12px;color:var(--muted);line-height:1.6}
.foot h4{font-size:17px;font-weight:500;margin-bottom:16px}
.foot li{list-style:none;font-size:13px;color:#333;line-height:32px}
.foot .links li{color:#777;font-size:12px}
.vline{width:1px;height:210px;background:var(--line)}
.input{width:238px;height:42px;border:1px solid #ddd;border-radius:22px;font-size:12px;color:#888;line-height:40px;padding-left:24px}
.social{display:flex;gap:12px}
.social i{display:block;width:12px;height:12px;border-radius:50%;background:var(--ink)}
.bottom-rule{left:86px;top:3966px;width:1027px;height:1px;background:var(--line)}
</style>
</head>
<body>
<div class="abs topbar">Service many customers from all over the world.Let's work together,win-win cooperation.<span class="close">×</span></div>

<header class="abs header">
  <div class="brand">Lovonna</div>
  <nav class="nav"><span>Home</span><span>Product ⌄</span><span>News</span><span>About Us</span><span>Contact Us</span><span>Send Inquiry</span></nav>
  <div class="icons">
    <svg viewBox="0 0 24 24"><circle cx="10" cy="10" r="7"/><path d="M15 15l6 6"/></svg>
    <svg viewBox="0 0 24 24"><circle cx="12" cy="8" r="4"/><path d="M4 21c1-5 5-7 8-7s7 2 8 7"/></svg>
    <svg viewBox="0 0 24 24"><rect x="7" y="2" width="10" height="20" rx="2"/><path d="M11 18h2"/></svg>
    <svg viewBox="0 0 24 24"><path d="M2 4h3l3 11h11l2-8H7"/><circle cx="9" cy="20" r="1.5"/><circle cx="18" cy="20" r="1.5"/></svg>
  </div>
</header>
<div class="cart-badge">0</div>

<div class="abs hero-left" role="img" aria-label="Soft blurred photo of a wedding invitation card on a table"></div>
<div class="abs hero-right" role="img" aria-label="Gold laser-cut floral wedding invitation with kraft envelope on wooden table"></div>
<div class="abs hero-copy">
  <h1>Happy Wedding Season</h1>
  <p>Pass you's happiness and joy in the important days of your life.</p>
  <span class="btn">Shop Now</span>
</div>
<div class="abs dots"><i></i><i></i><i></i></div>

<h2 class="abs section-title" style="top:690px">Our Popular Categories</h2>
<div class="abs cat" style="left:86px;top:775px;background:linear-gradient(135deg,#c79a62,#8a5a34)" role="img" aria-label="Gold lace wedding invitation card"><span>Wedding Invitation Card</span><b><svg width="24" height="10" viewBox="0 0 24 10" fill="none" stroke="#fff"><path d="M0 5h22M18 1l4 4-4 4"/></svg></b></div>
<div class="abs cat" style="left:437px;top:775px;background:linear-gradient(135deg,#cfe3e4,#7fb3bb)" role="img" aria-label="Laser cut favor boxes with ribbons"><span>Laser Cut Favor Box</span><b><svg width="24" height="10" viewBox="0 0 24 10" fill="none" stroke="#fff"><path d="M0 5h22M18 1l4 4-4 4"/></svg></b></div>
<div class="abs cat" style="left:788px;top:775px;background:linear-gradient(135deg,#e9e2d8,#b51f26 55%,#7a2a1a)" role="img" aria-label="Red laser cut wedding stationery card"><span>Wedding Stationery</span><b><svg width="24" height="10" viewBox="0 0 24 10" fill="none" stroke="#fff"><path d="M0 5h22M18 1l4 4-4 4"/></svg></b></div>
<div class="abs cat" style="left:86px;top:1096px;background:linear-gradient(135deg,#a7b48a,#e2b9b0 50%,#9fd6d4)" role="img" aria-label="Kraft, pink and blue gift tags"><span>Wedding Decoration Accessories</span><b><svg width="24" height="10" viewBox="0 0 24 10" fill="none" stroke="#fff"><path d="M0 5h22M18 1l4 4-4 4"/></svg></b></div>
<div class="abs cat" style="left:437px;top:1096px;background:linear-gradient(135deg,#8a6b52,#e8c2c6 50%,#b67884)" role="img" aria-label="Pink 3D pop up wedding card"><span>3D pop up card</span><b><svg width="24" height="10" viewBox="0 0 24 10" fill="none" stroke="#fff"><path d="M0 5h22M18 1l4 4-4 4"/></svg></b></div>
<div class="abs cat" style="left:788px;top:1096px;background:linear-gradient(135deg,#b48755,#2d3457 55%,#4a3a3a)" role="img" aria-label="Navy and gold laser cut greeting card"><span>Greeting card</span><b><svg width="24" height="10" viewBox="0 0 24 10" fill="none" stroke="#fff"><path d="M0 5h22M18 1l4 4-4 4"/></svg></b></div>

<section class="abs about">
  <h2>Hangzhou Blue Pine Stationery Co., Ltd.</h2>
  <p>Our company is established in 2001, located in Hang Zhou, Zhejiang Province.We are an professional manufacturer and exporter that is concerned with the design, development and production manufacturing wedding invitation card, favor boxes and other gift items.</p>
  <p>Our company products all passed the CE, FSC and BSCI accreditation.We are able to provide high-quality products to customers from around the world, main market areas include Europe(Germany, UK, France, Italy), USA, Asian(Japan, Korea, India), South America.We have always been the most trusted partner of our customers.</p>
</section>

<h2 class="abs section-title" style="top:1848px">New Product</h2>
<div class="abs prod" style="left:86px;top:1917px"><div class="img" style="background:linear-gradient(135deg,#b99873,#7e3a4f)" role="img" aria-label="Burgundy laser cut pocket invitation"></div><div class="name">Custom pocket card red invitations for wedding/anniversary/banquet</div><div class="price">$0.81 – $1.17</div></div>
<div class="abs prod" style="left:349px;top:1917px"><div class="img" style="background:linear-gradient(135deg,#d8cfc7,#f4f0ea)" role="img" aria-label="White laser cut invitation card"></div><div class="name">Elegant Laser cutting invitation card printable invitation paper with envelope</div><div class="price">$0.81 – $1.35</div></div>
<div class="abs prod" style="left:612px;top:1917px"><div class="img" style="background:linear-gradient(135deg,#c1a07d,#8c6b4f)" role="img" aria-label="Kraft pocket fold invitation set"></div><div class="name">Laser cut pocket fold invitations card for wedding/anniversary/banquet</div><div class="price">$0.81 – $1.17</div></div>
<div class="abs prod" style="left:876px;top:1917px"><div class="img" style="background:linear-gradient(135deg,#cfc6bd,#9d8270)" role="img" aria-label="Vintage kraft invitation with envelope"></div><div class="name">Vintage wedding invitation cards printable blank cards and envelopes</div><div class="price">$0.81 – $1.17</div></div>
<div class="abs prod" style="left:86px;top:2284px"><div class="img" style="background:linear-gradient(135deg,#e3dcd1,#c9c4c8)" role="img" aria-label="White lace pocket invitation with bow"></div><div class="name">Customize invitation pocket laser cut card for anniversal/banquet</div><div class="price">$0.80 – $1.35</div></div>
<div class="abs prod" style="left:349px;top:2284px"><div class="img" style="background:linear-gradient(135deg,#a88464,#eee7df)" role="img" aria-label="White rose folding invitation card"></div><div class="name">Laser cut elegant rose wedding banquet invitation card love folding card</div><div class="price">$0.80 – $1.33</div></div>
<div class="abs prod" style="left:612px;top:2284px"><div class="img" style="background:linear-gradient(135deg,#a37b57,#e8e1d8 55%,#c9a6b6)" role="img" aria-label="Hollow out invitation card with flowers"></div><div class="name">Hollow out invitations card for wedding/anniversary/banquet/event</div><div class="price">$1.12 – $1.58</div></div>
<div class="abs prod" style="left:876px;top:2284px"><div class="img" style="background:linear-gradient(135deg,#c2bbb4,#efebe6)" role="img" aria-label="White laser cut invitation with blank sheet"></div><div class="name">Elegant laser cut wedding invitation card with blank sheet and envelope</div><div class="price">$1.12 – $1.58</div></div>

<div class="abs video" role="img" aria-label="Showroom shelves full of invitation cards and favor boxes"></div>
<div class="abs play"><svg width="96" height="96" viewBox="0 0 96 96"><path d="M43 40l14 8-14 8z" fill="#222"/></svg></div>

<h2 class="abs section-title" style="top:3285px">From The Blog</h2>
<article class="abs blog" style="left:86px;top:3355px;width:499px">
  <div class="img" style="background:linear-gradient(135deg,#e7ece8,#3fa489 55%,#e9c9cf)" role="img" aria-label="Teal laser cut invitation with pink flowers"></div>
  <div class="txt"><div class="date"><svg width="14" height="14" viewBox="0 0 14 14" fill="none" stroke="#555"><circle cx="7" cy="7" r="6"/><path d="M7 3v4l3 2"/></svg>December 15, 2020</div>
  <h3>2020 The 18th Eastbay International Gifts, Premiums and Housewares Exhibition</h3>
  <p>Hangzhou Blue Pine Stationery Company attended The 18th Eastbay International Gifts, Premiums and Housewares Exhibition December, 2020</p></div>
</article>
<article class="abs blog" style="left:613px;top:3355px;width:500px">
  <div class="img" style="background:linear-gradient(135deg,#b08a62,#7e3a4f)" role="img" aria-label="Burgundy laser cut invitation with kraft envelope"></div>
  <div class="txt"><div class="date"><svg width="14" height="14" viewBox="0 0 14 14" fill="none" stroke="#555"><circle cx="7" cy="7" r="6"/><path d="M7 3v4l3 2"/></svg>April 27, 2019</div>
  <h3>2019 Harbour Gifts &amp; Premium Fair</h3>
  <p style="margin-top:36px">Hangzhou Blue Pine Stationery Company attended Harbour Gifts &amp; Premium Fair ,April,2019</p></div>
</article>

<footer>
  <div class="abs brand" style="left:86px;top:3722px">Lovonna</div>
  <p class="abs" style="left:86px;top:3792px;width:200px;font-size:12px;line-height:1.65">Rm B204, 3rd Floor, Songhe Building, Linpu Road, Hangzhou, P.R.CHINA, 310012</p>
  <p class="abs" style="left:86px;top:3866px;font-size:10px;color:#777;text-decoration:underline">Show on map</p>
  <div class="abs social" style="left:86px;top:3904px" aria-label="Social links"><i></i><i></i><i></i></div>
  <div class="abs vline" style="left:315px;top:3716px"></div>
  <div class="abs foot" style="left:360px;top:3722px"><h4>Telephone</h4><ul><li>+86 13700482915</li><li>+86 18600371942</li><li>+86 18655204718</li><li>+86 18733019265</li><li>+86 18733019265</li></ul></div>
  <div class="abs foot" style="left:522px;top:3722px"><h4>Email</h4><ul><li>office@bluepinecrafts.com</li><li>mara@bluepinecrafts.com</li><li>tessa@bluepinecrafts.com</li><li>ruby@bluepinecrafts.com</li><li>june@bluepine-cards.com</li></ul></div>
  <div class="abs foot links" style="left:731px;top:3722px"><ul><li>Home</li><li>Product</li><li>News</li><li>About Us</li><li>Contact Us</li><li>Send Inquiry</li></ul></div>
  <div class="abs vline" style="left:849px;top:3716px"></div>
  <div class="abs foot" style="left:879px;top:3722px"><h4>Join our newsletter</h4><div class="input">Your email Address</div><span class="btn" style="margin-top:16px;height:44px;line-height:44px">Subscribe</span></div>
  <div class="abs bottom-rule"></div>
  <p class="abs" style="left:86px;top:3990px;font-size:20px">+86 13700482915 <span style="font-size:12px">+86-05716230419(Mobile)</span></p>
  <p class="abs" style="left:622px;top:3996px;width:491px;text-align:right;font-size:11.5px">©2020 - 2033 Hangzhou Blue Pine Stationery Co., Ltd. (203502) All rights reserved</p>
</footer>
</body>
</html>
```